紅はるか、安納芋、紫芋、3種類を別々に芋バタージャムにしました。
シールは、共通です。シールの一部に紅はるか、安納芋、紫芋と別々に記載してもらいます。
容器は透明なスパウト付スタンドパウチKR72ーMB4815Qです
パンに塗ったり、ヨーグルトと共に食べていただきたいと思います。
●塗ってから焼くと、芋の香りがして美味しさが引き立ちます。
内容量150g 480円
瓶詰めにしなかった理由は、スタンドパウチは、パンに塗りやすい事と、使い終わってからの処理を考えてのことです。
●パウチに入れた事で、送料が格段に安くつくことです。
ナゴミメールで全国198円で送れます。

ネット販売あり
購買客層 芋好きな女性がターゲット

記載文書
メイン   ポムリ寄合
サブ    鹿児島
てんさい糖使用
無添加
紅はるかor紫イモor安納芋

シールの大きさ  最大 横50mm縦70mm
シールの形    丸、楕円、四角形、長方形
形は、問いません。

画像は、紅はるかの画像です。
安納芋は、もう少し赤みがかっています。
紫芋は、紫色です。

今回は、素晴らしい提案有難うございます。
ポムリ寄合の楽しいネーミングに、マッチした図案ができたと、社員一同喜んでいます。
遊び心を大事に、商品を手に取り読んでいただけるものになったと思います。
ワークリンデ初心者ですが、早々な対応にも感謝いたします。
機会があれば、よろしくお願いいたします。

今回は、ワークリンデ初心者にもかかわらず、沢山の方のご提案、感謝いたします。
皆様にうまくこちらの思いを伝えることがず、ご迷惑をお掛けしたことをお詫び申し上げます。
素晴らしい案件が多く、選ぶのに苦労しました。
こらからも、仕事依頼に使わせていただきます。
よろしくお願いいたします。

```html
<!DOCTYPE html>
<html lang="ja">
<head>
<meta charset="utf-8">
<title>ポムリ寄合 ラベル</title>
<link rel="stylesheet" href="https://fonts.googleapis.com/css2?family=M+PLUS+Rounded+1c:wght@500;800&family=Kosugi+Maru&display=swap">
<style>
  :root {
    --page: #ecebea;
    --label-top: #c2518b;
    --label-top-dark: #a63f76;
    --gingham: #efc4da;
    --gingham-light: #f8e2ee;
    --ribbon: #7fae3a;
    --ribbon-text: #f6f3d8;
    --potato: #8a4d6e;
    --footer-bg: #f6d9e7;
    --footer-text: #6b2f52;
    --white: #ffffff;
  }
  * { margin: 0; padding: 0; box-sizing: border-box; }
  html, body {
    width: 896px; height: 1200px; overflow: hidden;
    background: var(--page);
  }
  body { display: flex; align-items: center; justify-content: center; }
  .label {
    width: 780px; height: 820px;
    background: var(--label-top);
    border-radius: 22px;
    overflow: hidden;
    display: flex; flex-direction: column;
    font-family: "M PLUS Rounded 1c", sans-serif;
  }
  .label__head {
    position: relative;
    height: 360px;
    display: flex; flex-direction: column; align-items: center; justify-content: center;
  }
  .origin {
    position: absolute; left: 32px; top: 28px;
    display: inline-block;
    font-family: "Kosugi Maru", sans-serif;
    font-size: 30px; line-height: 1.2;
    white-space: nowrap;
    color: var(--white);
    background: var(--label-top-dark);
    padding: 6px 12px;
    border-radius: 10px;
    letter-spacing: 2px;
  }
  .brand {
    margin-top: 30px;
    color: var(--white);
    font-weight: 800;
    font-size: 140px; line-height: 1.05;
    text-align: center;
    letter-spacing: 6px;
  }
  .label__body {
    position: relative;
    flex: 1;
    background: linear-gradient(var(--gingham), var(--gingham-light));
    display: flex; flex-direction: column; align-items: center; justify-content: center;
  }
  .potatoes {
    width: 440px; height: 190px;
    border-radius: 40px;
    background: radial-gradient(ellipse at center, var(--potato) 0%, #a35f85 70%, transparent 100%);
  }
  .variety {
    position: relative;
    margin-top: -20px;
    background: var(--ribbon);
    color: var(--ribbon-text);
    font-family: "Kosugi Maru", sans-serif;
    font-size: 40px; line-height: 1.3; letter-spacing: 6px;
    padding: 8px 60px;
    border-radius: 8px;
    white-space: nowrap;
  }
  .label__foot {
    height: 90px;
    background: var(--footer-bg);
    display: flex; align-items: center; justify-content: center; gap: 60px;
    color: var(--footer-text);
    font-family: "Kosugi Maru", sans-serif;
    font-size: 40px; letter-spacing: 3px;
    white-space: nowrap;
  }
</style>
</head>
<body>
  <main class="label">
    <header class="label__head">
      <span class="origin">鹿児島</span>
      <h1 class="brand">ポムリ<br>寄合</h1>
    </header>
    <section class="label__body">
      <div class="potatoes" role="img" aria-label="三本の紫色のさつまいものイラスト"></div>
      <p class="variety">紅はるか</p>
    </section>
    <footer class="label__foot">
      <span>てんさい糖使用</span>
      <span>無添加</span>
    </footer>
  </main>
</body>
</html>
```